Graphic Design Project

We need a single page design that will be used as a regular white paper, providing communication advice & techniques.

We have an example that needs upgrading to look more professional and exciting.

Logo and icons will be provided.

Image provided for this example but will need to be able to add and remove new images relative to each new white paper.

Design will need to be on a format that is easily editable and can be converted into a PDF document. e.g MS Word.

Target Market(s)

Existing and potential corporate individuals and organisations

Industry/Entity Type

Communication

Requirements
Must have
• Logo, Icons & web address

```html
<!DOCTYPE html>
<html lang="en">
<head>
<meta charset="utf-8">
<title>Public Workshop – White Paper</title>
<link href="https://fonts.googleapis.com/css2?family=Didact+Gothic&family=Questrial&display=swap" rel="stylesheet">
<style>
  :root{
    --backdrop:#9b9b9b;
    --paper:#ffffff;
    --ink:#1f1f1f;
    --band:#b7b7b7;
    --footer-band:#bdbcbc;
    --sidebar:#6f6553;
    --medal-light:#8d6f45;
    --medal-dark:#5b4a33;
    --photo-light:#b9b2a2;
    --photo-dark:#5f5a52;
    --white:#ffffff;
  }
  *{margin:0;padding:0;box-sizing:border-box}
  html,body{width:1200px;height:1000px;overflow:hidden;background:var(--backdrop)}
  .canvas{position:relative;width:1200px;height:1000px;background:var(--backdrop);font-family:"Didact Gothic",sans-serif;color:var(--ink)}
  .page{position:absolute;left:213px;top:0;width:587px;height:832px;background:var(--paper)}
  .brand{position:absolute;left:218px;top:14px;display:flex;align-items:center;gap:16px}
  .brand-name{font-family:"Didact Gothic",sans-serif;font-size:50px;line-height:1;color:var(--ink);letter-spacing:-1px}
  .brand-dot{width:44px;height:44px;border-radius:50%;background:var(--medal-light)}
  .title-band{position:absolute;left:213px;top:118px;width:480px;height:39px;background:var(--band);
    font-family:"Questrial",sans-serif;font-size:22px;line-height:39px;padding-left:44px;color:var(--ink)}
  .column{position:absolute;top:175px;width:215px;font-size:9.6px;line-height:22.7px;text-align:justify;letter-spacing:-.15px}
  .column-left{left:262px}
  .column-right{left:531px}
  .footer-band{position:absolute;left:213px;top:832px;width:587px;height:168px;background:var(--footer-band);
    padding:23px 18px 0 19px;font-size:9.6px;line-height:23.4px;text-align:justify;letter-spacing:-.15px}
  .sidebar{position:absolute;left:800px;top:0;width:188px;height:1000px;background:var(--sidebar)}
  .event-medal{position:absolute;left:2px;top:-3px;width:186px;height:186px}
  .event-title{position:absolute;left:0;top:190px;width:188px;text-align:center;font-family:"Questrial",sans-serif;
    color:var(--white);font-size:32px;line-height:31px;transform:scaleX(.88)}
  .event-photo{position:absolute;left:0;top:728px;width:188px;height:272px;
    background:linear-gradient(180deg,var(--photo-light) 0%,#9c9484 45%,var(--photo-dark) 100%)}
</style>
</head>
<body>
<div class="canvas">
  <div class="page"></div>

  <div class="brand">
    <span class="brand-name">Brightline Advisory</span>
    <span class="brand-dot"></span>
  </div>

  <h1 class="title-band">Lorem ipsum dolor sit amet, consectetur.</h1>

  <div class="column column-left">
    <p>Lorem ipsum dolor sit amet, consectetur adipiscing elit. Donec mattis tincidunt tempor. Sed ullamcorper massa eget justo lacinia sit amet sagittis odio tempor. Phasellus adipiscing neque ut metus commodo eu posuere purus sollicitudin. Cras eu nibh justo. Quisque blandit placerat nisl, non vestibulum ipsum pretium vehicula. Etiam dignissim felis sed risus varius ac scelerisque massa aliquam. Aenean dignissim sagittis lacus vel porta. Pellentesque non diam leo. Donec semper dolor elementum metus cursus in tincidunt magna sagittis. Aenean sagittis tincidunt quam, non blandit elit posuere eget. Ut imperdiet urna non dolor interdum non interdum nibh lobortis. Suspendisse potenti.</p>
    <p>Etiam non scelerisque justo. Vivamus sit amet tellus massa. Cum sociis natoque penatibus et magnis dis parturient montes, nascetur ridiculus mus. Mauris dolor lorem, ornare in sagittis a, rhoncus ac urna. Sed eget sem in purus scelerisque rutrum. Aliquam erat volutpat. Duis adipiscing nulla suscipit purus condimentum non pellentesque nisi lobortis. Morbi elementum pellentesque elementum. Maecenas lobortis lacinia lacus, at elementum turpis tempor at.</p>
    <p>Sed odio ligula, faucibus a tristique et, convallis ac mi. Nulla pharetra nisl sed nisi fermentum adipiscing. Vivamus non blandit quam. Suspendisse iaculis consectetur est eget consequat. Morbi interdum, velit in auctor aliquet, tortor nisl semper elit, in iaculis urna mauris vitae massa.</p>
  </div>

  <div class="column column-right">
    <p>Lorem ipsum dolor sit amet, consectetur adipiscing elit. Donec mattis tincidunt tempor. Sed ullamcorper massa eget justo lacinia sit amet sagittis odio tempor. Phasellus adipiscing neque ut metus commodo eu posuere purus sollicitudin. Cras eu nibh justo. Quisque blandit placerat nisl, non vestibulum ipsum pretium vehicula. Etiam dignissim felis sed risus varius ac scelerisque massa aliquam. Aenean dignissim sagittis lacus vel porta. Pellentesque non diam leo. Donec semper dolor elementum metus cursus in tincidunt magna sagittis. Aenean sagittis tincidunt quam, non blandit elit posuere eget. Ut imperdiet urna non dolor interdum non interdum nibh lobortis. Suspendisse potenti.</p>
    <p>Etiam non scelerisque justo. Vivamus sit amet tellus massa. Cum sociis natoque penatibus et magnis dis parturient montes, nascetur ridiculus mus. Mauris dolor lorem, ornare in sagittis a, rhoncus ac urna. Sed eget sem in purus scelerisque rutrum. Aliquam erat volutpat. Duis adipiscing nulla suscipit purus condimentum non pellentesque nisi lobortis. Morbi elementum pellentesque elementum. Maecenas lobortis lacinia lacus, at elementum turpis tempor at.</p>
    <p>Sed odio ligula, faucibus a tristique et, convallis ac mi. Nulla pharetra nisl sed nisi fermentum adipiscing. Vivamus non blandit quam. Suspendisse iaculis consectetur est eget consequat. Morbi interdum, velit in auctor aliquet, tortor nisl semper elit, in iaculis urna mauris vitae massa.</p>
  </div>

  <div class="footer-band">
    <p>Vestibulum elit urna, consectetur vitae sodales non, pretium a felis. In adipiscing, dui sed gravida luctus, neque lorem blandit ipsum, ac convallis odio nisi id dui. Aenean ac velit eget magna lobortis molestie. Praesent ullamcorper vehicula aliquet. Donec nisl sem, vulputate vitae egestas nec, egestas iaculis risus. Mauris et volutpat ligula. Vestibulum elit urna, consectetur vitae sodales non, pretium a felis. In adipiscing, dui sed gravida luctus, neque lorem blandit ipsum, ac convallis odio nisi id dui. Aenean ac velit eget magna lobortis molestie. Praesent ullamcorper vehicula aliquet. Donec nisl sem, vulputate vitae egestas nec, egestas iaculis risus. Mauris et volutpat ligula.</p>
  </div>

  <aside class="sidebar">
    <svg class="event-medal" viewBox="0 0 186 186" role="img" aria-label="Public workshop emblem">
      <defs>
        <radialGradient id="medalFill" cx="50%" cy="35%" r="65%">
          <stop offset="0%" stop-color="var(--medal-light)"/>
          <stop offset="100%" stop-color="var(--medal-dark)"/>
        </radialGradient>
      </defs>
      <circle cx="93" cy="93" r="93" fill="url(#medalFill)"/>
    </svg>
    <div class="event-title">PUBLIC<br>WORKSHOP</div>
    <div class="event-photo" role="img" aria-label="Photo of participants seated around a conference table during a workshop"></div>
  </aside>
</div>
</body>
</html>
```